Harborline Quoting
Business Cards and Stationery for Service Co
Simple
Dane Corwell
Vice President
20436 SW 47th Avenue Suite 3105 Vancouver, WA 97531
danec@harborlinequoting.com
www.harborlinequoting.com
Please keep it simple and professional.
Just the logo

```html
<!DOCTYPE html>
<html lang="en">
<head>
<meta charset="utf-8">
<title>Harborline Quoting – Business Card</title>
<link rel="stylesheet" href="https://fonts.googleapis.com/css2?family=Montserrat:wght@400;800&display=swap">
<style>
  :root {
    --brand-orange: #d9552b;
    --ink: #4a4a4a;
    --ink-soft: #6b6b6b;
    --paper: #ffffff;
    --backdrop: #e4e4e4;
    --rule: #9a9a9a;
    --tint: #f6d9d1;
  }
  * { box-sizing: border-box; margin: 0; padding: 0; }
  html, body { width: 1200px; height: 987px; overflow: hidden; }
  body {
    background: var(--backdrop);
    font-family: "Montserrat", Arial, sans-serif;
    position: relative;
  }
  .card {
    position: absolute;
    left: 220px;
    width: 760px;
    height: 434px;
    border-radius: 26px;
    overflow: hidden;
    box-shadow: 0 6px 18px rgba(0,0,0,0.18);
  }
  .card--front { top: 40px; background: var(--brand-orange); }
  .card--back  { top: 513px; background: var(--paper); }

  /* wordmark */
  .wordmark {
    display: flex;
    align-items: center;
    gap: 18px;
    font-weight: 800;
    text-transform: uppercase;
  }
  .wordmark__dot { border-radius: 50%; flex: none; }
  .wordmark__name { line-height: 1; }
  .wordmark__line2 { display: block; letter-spacing: 0.42em; }

  .card--front .wordmark {
    position: absolute;
    left: 50%; top: 50%;
    transform: translate(-50%, -50%);
    color: var(--paper);
  }
  .card--front .wordmark__dot { width: 84px; height: 84px; background: var(--paper); }
  .card--front .wordmark__name { font-size: 58px; }
  .card--front .wordmark__line2 { font-size: 26px; margin-top: 8px; }

  .card--back .wordmark {
    position: absolute;
    left: 40px; top: 42px;
    color: var(--brand-orange);
    gap: 12px;
  }
  .card--back .wordmark__dot { width: 46px; height: 46px; background: var(--brand-orange); }
  .card--back .wordmark__name { font-size: 32px; }
  .card--back .wordmark__line2 { font-size: 14px; margin-top: 4px; }

  .backdrop-mark {
    position: absolute;
    right: 60px; top: 150px;
    width: 230px; height: 230px;
    border-radius: 50%;
    background: var(--tint);
    opacity: 0.7;
  }

  .person { position: absolute; left: 40px; top: 116px; }
  .person__name { font-size: 26px; font-weight: 400; color: var(--ink); }
  .person__title { font-size: 14px; color: var(--brand-orange); margin-top: 2px; }

  .divider {
    position: absolute;
    left: 40px; right: 40px; top: 268px;
    height: 1px; background: var(--rule);
  }

  .contact {
    position: absolute;
    font-size: 14px;
    line-height: 1.6;
    color: var(--ink-soft);
    font-weight: 400;
  }
  .contact--address { left: 40px; top: 176px; }
  .contact--reach { right: 40px; top: 292px; text-align: right; }
  .contact--web { left: 40px; top: 292px; }
</style>
</head>
<body>
  <section class="card card--front" aria-label="Card front">
    <div class="wordmark">
      <span class="wordmark__dot"></span>
      <span class="wordmark__name">Harborline<span class="wordmark__line2">Quoting</span></span>
    </div>
  </section>

  <section class="card card--back" aria-label="Card back">
    <div class="backdrop-mark" aria-hidden="true"></div>
    <div class="wordmark">
      <span class="wordmark__dot"></span>
      <span class="wordmark__name">Harborline<span class="wordmark__line2">Quoting</span></span>
    </div>
    <div class="person">
      <p class="person__name">Dane Corwell</p>
      <p class="person__title">Vice President</p>
    </div>
    <address class="contact contact--address" style="font-style:normal">
      20436 SW 47th Avenue<br>
      Suite 3105<br>
      Vancouver, WA 97531
    </address>
    <div class="divider"></div>
    <p class="contact contact--web">www.harborlinequoting.com</p>
    <p class="contact contact--reach">
      Tell: 360-555-0142<br>
      Fax: 888-555-0187<br>
      Email: danec@harborlinequoting.com
    </p>
  </section>
</body>
</html>
```